Crestwave Folio Network Presents… CFNMerit.com

I. The purpose of the phase1 is to gain access to (and control of) scholastic academic works that had been written and authored by students, but only after they have been corrected (vetted), by education professionals and returned to the student as corrected documents. It is my goal to push the CFN Merit Annual as inducements to have students turn over these papers and receive recognition and authorship, for these intellectual works.

Target Market(s)

university students
high school students

Number of Pages Required

2 page

Font styles to use
Serif
Sans Serif

Colors

Designer to choose colors to be used in the design.

Requirements
Must have
• must include this or similar language.
• Crestwave Folio Network Presents…
• CFNMerit.com
• Here is the assemblage of your academic successes. We collect and archive your written academic achievements, you’re “A” graded as correct, written assignments throughout the year, and when it’s over, we amass your academic documents into a bound book… your Brightmark Annual.
• You study hard and work hard all year trying to achieve the highest grades possible. At the end of the year, semester, or term you will have lasting proof to show what you did to achieve your academic excellence… and in book form too!
• Consider this the perfect gift to yourself to celebrate your ascendency and to showcase all of the hard work that you have put into getting to the next step on the ladder to success, your success.
• One good thing about this is that you don’t have to do any extra work to write your book. Once your written assignment has been reviewed, graded by an education authority and returned to you, all you do is to submit it to your registered account with us, add a brief description or special detail and we will add it to your database to build your success story.
• Our mission here is to track and highlight your academic successes. We want to honor and immortalize you through your academic “A” papers. Currently, once your term papers, research papers, writing assignments, book reports, studies, critiques, essays, theses, dissertations and the like, have been graded and returned back to you they soon become of no further value to you. But now with the Brightmark Annual you have a system available to you that can and will create a lasting record or Yearbook to catalogue what molded you into the intellectual that you have become. Once your academic papers have been evaluated by the scholastic authority and graded accordingly, you only have to post or download these materials as they become available to you. As you repeat the process again and again the storehouse of your knowledge legacy grows exponentially and become more relevant and valuable as entries into your Brightmark Annual.
• Imagine if you will, if there was a written record of Kowalczyk’s early studies and writings, from before he became the Kowalczyk that we know of today, or the Lindqvist’s early school and college writings? Just think of the value that these priceless gifts would hold today. Well you may say “but I’m not famous. Who would be interested in my schoolwork or assignments?” We can’t say for sure right now because the future is not known today. But we do know that years of study and research molded and shaped the Lindqvists from their modest upbringing and that Kowalczyk struggled for many years trying to get his thoughts and writings accepted by the establishment before they finally realized that “e” really did equal “mc2” (e=mc2). Who Knew? But you don’t have to become famous to be relevant. What value would you place on old mementos and writings of your parents, grand or great grandparents from before Vietnam or WWIl or??? I’m sure Kinrootly.com would kill to have access to these treasures. And so would your kids or descendants in future years. Yes, you are relevant and you can make a lasting difference if you create an enduring legacy. Together we can create that legacy.
• “Log on to: CFNMerit.com to comprehend what all the excitement is all about.”
• We are the vehicle to deliver your curriculum based study writings to you in the easiest and most hassle free way possible. As members of the Brightmark community your papers will always be available to you. Periodically this material will be compiled, configured if necessary, and formatted into book form as your personalized Brightmark Annual matures.
Nice to have
• very professional but student friendly graphes
Should not have
• leave out the affiliate program at this time.

```html
<!DOCTYPE html>
<html lang="en">
<head>
<meta charset="utf-8">
<title>CFNMerit.com</title>
<link rel="stylesheet" href="https://fonts.googleapis.com/css2?family=Montserrat:wght@400;500;600;700&family=Roboto:wght@400;500&family=Open+Sans:wght@400&display=swap">
<style>
:root{
  --green:#0b8a3e;
  --blue:#1a63c6;
  --hero-a:#1d5a9e;
  --hero-b:#3f7fc0;
  --page:#f5f5f5;
  --white:#ffffff;
  --navy:#03213f;
  --rule:#c9c9c9;
  --dark-a:#1b2a2c;
  --dark-b:#4a5a58;
}
*{margin:0;padding:0;box-sizing:border-box}
html,body{width:1200px;height:3197px;overflow:hidden}
body{position:relative;background:var(--page);font-family:"Montserrat",sans-serif;color:var(--blue)}
.abs{position:absolute}
.hero{left:0;top:0;width:1200px;height:725px;background:linear-gradient(160deg,var(--hero-b) 0%,var(--hero-a) 55%,#2c6aae 100%)}
.brand{left:26px;top:44px;font:700 38px "Montserrat",sans-serif;color:var(--white)}
.nav{top:58px;right:0;width:700px;display:flex;justify-content:flex-end;gap:0}
.nav a{color:var(--white);text-decoration:none;font:400 21px "Montserrat",sans-serif}
.nav a.home{position:absolute;left:0}
.hero-title{left:0;width:1200px;top:272px;text-align:center;font:700 64px "Montserrat",sans-serif;color:var(--white)}
.search{left:407px;top:402px;width:480px;height:57px;border-radius:29px;background:var(--white);display:flex;align-items:center;padding-left:36px;font:400 19px "Montserrat",sans-serif;color:#9a9a9a}
.search-btn{right:5px;top:5px;width:47px;height:47px;border-radius:50%;background:var(--green)}
.dots{left:543px;top:534px;display:flex;gap:24px}
.dots span{width:22px;height:22px;border-radius:50%;background:#dfe7f0}
.dots span.on{background:var(--green)}
.card{background:var(--white);box-shadow:0 4px 14px rgba(0,0,0,.12)}
.what{left:243px;top:629px;width:712px;height:447px}
.what h2{position:absolute;top:68px;width:100%;text-align:center;font:500 42px "Roboto",sans-serif;color:var(--green)}
.rule{height:2px;background:var(--rule)}
.rule i{position:absolute;top:-1px;height:3px;background:var(--blue)}
.what .rule{position:absolute;left:122px;top:143px;width:468px}
.what p{position:absolute;left:50px;top:168px;width:612px;text-align:center;font:400 20px/42px "Montserrat",sans-serif}
.what p b{color:var(--green);font-weight:400}
.track{left:0;width:1200px;top:1127px;text-align:center;font:500 44px "Roboto",sans-serif;color:var(--green)}
.track-rule{left:176px;top:1210px;width:877px}
.feature{width:560px;text-align:center;font:400 20px/42px "Montserrat",sans-serif}
.band{left:0;top:1730px;width:1200px;height:665px}
.band-title{left:0;width:1200px;top:1858px;text-align:center;font:400 52px "Montserrat",sans-serif;color:var(--white)}
.band-rule{left:190px;top:1983px;width:876px;background:#d8d8d8}
.band p{position:absolute}
.how-text{left:140px;top:2021px;width:980px;text-align:center;font:400 21px/42px "Montserrat",sans-serif;color:var(--white)}
.vehicle{left:134px;top:2412px;width:963px;height:309px}
.vehicle p{position:absolute;left:30px;top:48px;width:903px;text-align:center;font:600 19.5px/42px "Montserrat",sans-serif}
.cta{left:320px;top:2760px;width:639px;height:87px;border-radius:44px;background:var(--green);color:var(--white);display:flex;align-items:center;justify-content:center;font:600 28px "Montserrat",sans-serif}
.footer{left:0;top:2898px;width:1200px;height:299px;background:var(--navy);color:var(--white);font-family:"Open Sans",sans-serif}
.footer h4{position:absolute;top:36px;font:400 21px "Montserrat",sans-serif}
.footer ul{position:absolute;top:90px;list-style:none;font-size:21px;line-height:29px}
.footer .base{position:absolute;left:0;top:228px;width:1200px;height:1px;background:#3a5777}
.footer small{position:absolute;top:248px;font-size:16px}
</style>
</head>
<body>
<header class="abs hero" role="img" aria-label="Photograph of a hand writing with a pen on paper, tinted blue"></header>
<div class="abs brand">CFNMerit.com</div>
<nav class="abs nav" style="left:608px;top:58px;width:560px;height:30px">
  <a class="home" href="#" style="left:0">Home</a>
  <a href="#" style="position:absolute;left:97px">About Us</a>
  <a href="#" style="position:absolute;left:223px">What we do</a>
  <a href="#" style="position:absolute;left:390px">Sign Up</a>
  <a href="#" style="position:absolute;left:503px">Login</a>
</nav>
<h1 class="abs hero-title">We put the profit in Learning</h1>
<div class="abs search">Type text to search
  <span class="abs search-btn"><svg width="47" height="47" viewBox="0 0 47 47"><path d="M20 15l9 8.5-9 8.5" fill="none" stroke="#fff" stroke-width="4" stroke-linecap="round" stroke-linejoin="round"/></svg></span>
</div>
<div class="abs dots"><span class="on"></span><span></span><span></span></div>

<section class="abs card what">
  <h2>What CFNMerit Do</h2>
  <div class="rule"><i style="left:156px;width:180px"></i></div>
  <p>We collect and archive your written academic achievements, you’re “A” graded as correct, written assignments throughout the year, and when it’s over, we amass your academic documents into a bound book… your <b>CFN Merit Annual.</b></p>
</section>

<h2 class="abs track">Track you annual Achievements</h2>
<div class="abs rule track-rule"><i style="left:280px;width:310px"></i></div>

<svg class="abs" style="left:220px;top:1285px" width="148" height="142" viewBox="0 0 148 142" aria-hidden="true">
  <path d="M6 18 Q40 6 70 20 V128 Q40 114 6 126Z M78 20 Q108 6 142 18 V126 Q108 114 78 128Z" fill="var(--green)"/>
  <path d="M0 30 V138 H148 V30 H142 V132 H6 V30Z" fill="var(--green)"/>
</svg>
<p class="abs feature" style="left:14px;top:1447px">You study hard and work hard all year trying to achieve the highest grades possible. At the end of the year, semester, or term you will have lasting proof to show what you did to achieve your academic excellence… and in book form too!</p>

<svg class="abs" style="left:830px;top:1278px" width="140" height="150" viewBox="0 0 140 150" aria-hidden="true">
  <path d="M70 30 C50 2 30 8 36 22 C40 32 58 32 70 30 C82 32 100 32 104 22 C110 8 90 2 70 30Z" fill="none" stroke="var(--green)" stroke-width="8"/>
  <rect x="2" y="34" width="136" height="30" fill="var(--green)"/>
  <rect x="12" y="70" width="116" height="80" fill="var(--green)"/>
  <rect x="62" y="34" width="16" height="116" fill="var(--page)"/>
</svg>
<p class="abs feature" style="left:625px;top:1447px;width:560px">Consider this the perfect gift to yourself to celebrate your ascendency and to showcase all of the work that you have put into getting to the next step on the ladder to success, your success</p>

<svg class="abs band" viewBox="0 0 1200 665" width="1200" height="665">
  <defs>
    <linearGradient id="bandShade" x1="0" y1="0" x2="1" y2="0.3">
      <stop offset="0" stop-color="var(--dark-a)"/>
      <stop offset="0.55" stop-color="var(--dark-b)"/>
      <stop offset="1" stop-color="var(--dark-a)"/>
    </linearGradient>
  </defs>
  <polygon role="img" aria-label="Photograph of a student using a tablet, darkened" points="0,72 600,7 1200,72 1200,562 600,657 0,562" fill="url(#bandShade)"/>
  <polyline points="0,72 600,7 1200,72" fill="none" stroke="var(--blue)" stroke-width="9"/>
  <polyline points="0,562 600,657 1200,562" fill="none" stroke="var(--green)" stroke-width="9"/>
</svg>
<h2 class="abs band-title">How it works</h2>
<div class="abs rule band-rule"><i style="left:290px;width:300px;background:#8fb0c9"></i></div>
<p class="abs how-text">One good thing about this is that you don’t have to do any extra work to write your book. Once your written assignment has been reviewed, graded by an education authority and returned to you, all you do is to submit it to your registered account with us, add a brief description or special detail and we will add it to your database to build your success story.</p>

<section class="abs card vehicle">
  <p>We are the vehicle to deliver your curriculum based study writings to you in the easiest and most hassle free way possible. Log on to comprehend what all the excitement is all about. As a member of the CFN Merit community your papers will always be available to you. Periodically this material will be compiled, edited if necessary, and formatted into book form as your personalized CFN Merit Annual matures.</p>
</section>

<a class="abs cta">Get Your CFN Merit Annual Now</a>

<footer class="abs footer">
  <h4 style="left:83px">QUICK LINKS</h4>
  <ul style="left:83px"><li>Home</li><li>About Us</li><li>Services</li><li>News</li></ul>
  <h4 style="left:335px">CONTACT US</h4>
  <ul style="left:335px"><li>Email: hello@cfnmerit.com</li><li>Tel: (020) 5550 1842</li><li>Street: 12 Larkspur Row, Home Town</li></ul>
  <h4 style="left:921px">LOCATION MAP</h4>
  <div class="base"></div>
  <small style="left:20px">Copyright © 2018 CFN Merit. All rights reserved</small>
  <small style="left:912px">Terms Of Service | Privacy Policy</small>
</footer>
</body>
</html>
```